Quarrydeen Fintech Product Infographic

Quarrydeen is an established Fintech business, supplying complex financial software to banks and building societies.

We currently have a picture/infographic to show each of our 11 different software products in a single image. Each product can be installed on its own as a standalone application or if multiple products are installed they will share data.

The key message for our infographic is to convey the integration via a shared database.

The attached diagram is what we currently use which is to give you an idea of the message we are trying to give, but we are not tied to this format and are looking for this diagram to be reimagined.

We will look to use our new chosen design on printed media such as A4 Data sheets an example of which is attached.

For more information on our products please refer to www.quarrydeen.co.uk/products

```html
<!DOCTYPE html>
<html lang="en">
<head>
<meta charset="utf-8">
<title>Quarrydeen Fintech Product Infographic</title>
<link rel="stylesheet" href="https://fonts.googleapis.com/css2?family=Oswald:wght@500;600&family=Montserrat:wght@500&display=swap">
<style>
  :root {
    --bg: #ffffff;
    --performance: #c47fb8;
    --performance-deep: #b06ba4;
    --finance: #6fcdf0;
    --finance-deep: #58bce2;
    --risk: #fdb94f;
    --risk-deep: #f0a63c;
    --regulatory: #63c28e;
    --regulatory-deep: #4fb07a;
    --hub-text: #666666;
    --item-text: #555555;
  }
  html, body {
    margin: 0;
    padding: 0;
    width: 1200px;
    height: 564px;
    overflow: hidden;
    background: var(--bg);
  }
  .infographic { display: block; width: 1200px; height: 564px; }
  .group-title {
    font-family: "Oswald", sans-serif;
    font-weight: 500;
    font-size: 22px;
    letter-spacing: 0.2px;
  }
  .product {
    font-family: "Montserrat", sans-serif;
    font-weight: 500;
    font-size: 19px;
    fill: var(--item-text);
  }
  .hub-label {
    font-family: "Oswald", sans-serif;
    font-weight: 500;
    font-size: 38px;
    fill: var(--hub-text);
  }
  .icon { fill: none; stroke: #fff; stroke-width: 2.6; stroke-linejoin: round; stroke-linecap: round; }
  .leader { stroke-width: 1.3; }
  .performance .group-title { fill: var(--performance); }
  .finance .group-title { fill: var(--finance); }
  .risk .group-title { fill: var(--risk); }
  .regulatory .group-title { fill: var(--regulatory); }
  .performance .leader { stroke: var(--performance); }
  .finance .leader { stroke: var(--finance); }
  .risk .leader { stroke: var(--risk); }
  .regulatory .leader { stroke: var(--regulatory); }
</style>
</head>
<body>
<svg class="infographic" viewBox="0 0 1200 564" xmlns="http://www.w3.org/2000/svg" role="img" aria-label="Quarrydeen products sharing one data store">
  <defs>
    <filter id="hub-shadow" x="-30%" y="-30%" width="160%" height="160%">
      <feDropShadow dx="0" dy="3" stdDeviation="5" flood-color="#000" flood-opacity="0.25"/>
    </filter>
    <radialGradient id="hub-fill" cx="50%" cy="35%" r="65%">
      <stop offset="0" stop-color="#ffffff"/>
      <stop offset="0.75" stop-color="#f7f7f7"/>
      <stop offset="1" stop-color="#e4e4e4"/>
    </radialGradient>
  </defs>

  <g class="wheel">
    <path d="M561 280 L405 280 A156 156 0 0 1 561 124 Z" fill="var(--performance)"/>
    <path d="M571 280 L571 124 A156 156 0 0 1 727 280 Z" fill="var(--finance)"/>
    <path d="M561 290 L561 446 A156 156 0 0 1 405 290 Z" fill="var(--risk)"/>
    <path d="M571 290 L727 290 A156 156 0 0 1 571 446 Z" fill="var(--regulatory)"/>

    <path d="M561 280 L467 280 A94 94 0 0 1 561 186 Z" fill="var(--performance-deep)"/>
    <path d="M571 280 L571 186 A94 94 0 0 1 665 280 Z" fill="var(--finance-deep)"/>
    <path d="M561 290 L561 384 A94 94 0 0 1 467 290 Z" fill="var(--risk-deep)"/>
    <path d="M571 290 L665 290 A94 94 0 0 1 571 384 Z" fill="var(--regulatory-deep)"/>

    <circle cx="566" cy="285" r="79" fill="url(#hub-fill)" filter="url(#hub-shadow)"/>
    <text class="hub-label" x="566" y="283" text-anchor="middle">SHARED</text>
    <text class="hub-label" x="566" y="322" text-anchor="middle">DATA</text>
  </g>

  <g class="icon">
    <rect x="452" y="212" width="7" height="14"/>
    <rect x="463" y="204" width="7" height="22"/>
    <rect x="474" y="196" width="7" height="30"/>
    <path d="M447 199 L458 189 L464 193 L476 183"/>
    <path d="M470 183 L477 182 L476 189"/>
    <rect x="645" y="214" width="7" height="12"/>
    <rect x="656" y="205" width="7" height="21"/>
    <rect x="667" y="194" width="7" height="32"/>
    <path d="M477 340 L500 380 L454 380 Z"/>
    <path d="M477 355 L477 367"/>
    <circle cx="477" cy="373" r="0.8"/>
    <path d="M648 347 L670 347 L678 355 L678 383 L648 383 Z"/>
    <path d="M670 347 L670 355 L678 355"/>
    <path d="M654 362 L672 362 M654 368 L672 368 M654 374 L672 374"/>
  </g>

  <g class="group performance">
    <text class="group-title" x="425" y="168" text-anchor="end">PERFORMANCE</text>
    <text class="product" x="397" y="202" text-anchor="end">Financial Planning</text>
    <text class="product" x="382" y="235" text-anchor="end">Funds Transfer Pricing</text>
    <text class="product" x="374" y="267" text-anchor="end">Business Intelligence</text>
    <line class="leader" x1="406" y1="196" x2="440" y2="196"/>
    <line class="leader" x1="392" y1="229" x2="416" y2="229"/>
    <line class="leader" x1="383" y1="261" x2="410" y2="261"/>
  </g>

  <g class="group finance">
    <text class="group-title" x="716" y="168">FINANCE</text>
    <text class="product" x="741" y="202">Financial Ledgers</text>
    <text class="product" x="757" y="235">Effective Interest Rates</text>
    <text class="product" x="762" y="267">Hedges Accounting</text>
    <line class="leader" x1="695" y1="196" x2="728" y2="196"/>
    <line class="leader" x1="710" y1="229" x2="747" y2="229"/>
    <line class="leader" x1="725" y1="261" x2="752" y2="261"/>
  </g>

  <g class="group risk">
    <text class="group-title" x="387" y="321" text-anchor="end">RISK</text>
    <text class="product" x="382" y="355" text-anchor="end">Treasury</text>
    <text class="product" x="386" y="387" text-anchor="end">ALM</text>
    <line class="leader" x1="397" y1="349" x2="442" y2="349"/>
    <line class="leader" x1="397" y1="381" x2="442" y2="381"/>
  </g>

  <g class="group regulatory">
    <text class="group-title" x="741" y="321">REGULATORY</text>
    <text class="product" x="754" y="355">Regulatory Reporting</text>
    <text class="product" x="754" y="387">Taxation Reporting</text>
    <text class="product" x="740" y="420">DPGS SCV</text>
    <line class="leader" x1="704" y1="349" x2="746" y2="349"/>
    <line class="leader" x1="694" y1="381" x2="746" y2="381"/>
    <line class="leader" x1="662" y1="414" x2="728" y2="414"/>
  </g>
</svg>
</body>
</html>
```